Zielgruppe
Wir sind eine Imkerei mit angeschlossenem Lehrgarten. Unsere Produktpalette umfasst selbst hergestellte Imkereiprodukte aller Art (Honig, Bienenwachskerzen, Propolis, Pollen, Met). Unsere Zielgruppe sind solvente, umweltbewusste Konsumenten mit dem Sinn für nachhaltig und regional produzierte Waren.
Aufgabenstellung
- Das Etikett soll maximal die Logo-Farben nutzen (weiß, schwarz, gelb), evtl. mit goldenen Akzenten.
- Logo 'Imkerei Fam. Halvers' integrieren
- Ein gleich aussehendes Grundetikett für mehrere Sorten
- Honigname 'Dünenglanz' + Sortenbezeichnung (Rapshonig, Frühtrachthonig, Sommertrachthonig), zusätzlich ein 'Leeretikett' zum Einstempeln von Sondersorten
- Optische Elemente gerne Waben und/oder Regionales (Friesland, Jadebusen, Nordsee)
- Wir erweitern Stück für Stück unser Sortiment, daher soll das Grunddesign später auf Etiketten für zum Beispiel Met, Seife und Bonbons auszuweiten sein.
- Etiketten in 3 verschiedenen Größen nutzbar (500g, 250g, 50g)
- Pflichtangaben auf Honigetiketten: Deutscher Honig/ Honig aus Deutschland, Füllmenge (Schriftgröße mind. 4 mm Höhe), Hersteller/ Name und Anschrift des Imkers (zunächst Platzhalter nutzen, Daten werden im Verlauf übermittelt), Platz für Datumsstempel (MHD), Lagerbedingung (kühl, trocken und dunkel lagern)
- Das Etikett soll einen Gewährverschluss haben, obenauf das leere Feld für den Datumsstempel
- Das Honigglas hat einen goldenen Deep Twist Off Deckel

```html
<!DOCTYPE html>
<html lang="de">
<head>
<meta charset="utf-8">
<title>Dünenglanz – Honigetiketten Imkerei Fam. Halvers</title>
<link href="https://fonts.googleapis.com/css2?family=Libre+Baskerville&family=Roboto+Condensed:wght@400;700&display=swap" rel="stylesheet">
<style>
  :root {
    --bg: #ffffff;
    --label: #ffffff;
    --edge: #d9d9d9;
    --ink: #2b2622;
    --brand: #3b3026;
    --yellow: #f4b41a;
    --green: #9dbb3a;
    --comb: #e6e6e6;
    --rule: #9a9a9a;
    --sans: "Roboto Condensed", "Arial Narrow", sans-serif;
    --serif: "Libre Baskerville", Georgia, serif;
  }
  * { box-sizing: border-box; margin: 0; padding: 0; }
  html, body { width: 1200px; height: 923px; overflow: hidden; background: var(--bg); }
  .canvas { position: relative; width: 1200px; height: 923px; font-family: var(--sans); color: var(--ink); }

  /* tamper seal */
  .seal {
    position: absolute; left: 278px; top: 30px; width: 244px; height: 244px;
    border-radius: 50%; background: var(--label); border: 14px solid var(--yellow);
    text-align: center; z-index: 2;
  }
  .seal .brand-name { margin-top: 58px; }
  .seal .divider { width: 110px; height: 1px; background: var(--rule); margin: 12px auto 12px; }
  .seal .mhd-label { font-size: 10px; }
  .seal .mhd-date { font-size: 15px; letter-spacing: .5px; margin-top: 4px; color: #555; }

  .tab { position: absolute; width: 118px; }
  .tab-yellow { left: 322px; top: 262px; height: 292px;
    background: linear-gradient(to bottom, var(--yellow) 0, var(--yellow) 150px, transparent 150px); }
  .tab-yellow::after { content: ""; position: absolute; left: 0; top: 150px; width: 118px; height: 30px;
    background: linear-gradient(to bottom right, var(--yellow) 50%, transparent 50%); }
  .tab-green { left: 915px; top: 393px; height: 161px;
    background: linear-gradient(to bottom right, var(--green) 50%, transparent 50%) 0 0 / 118px 40px no-repeat; }
  .tab-white { position: absolute; background: var(--label); border-left: 1px solid var(--edge); border-right: 1px solid var(--edge); }

  /* wrap label */
  .label { position: absolute; top: 554px; height: 271px; background: var(--label); border: 1px solid var(--edge); }
  .label--full { left: 41px; width: 675px; }
  .label--front { left: 775px; width: 394px; }

  .comb { position: absolute; background: linear-gradient(135deg, var(--comb), rgba(230,230,230,0)); opacity: .8; }

  .wing-left { position: absolute; left: 18px; top: 72px; width: 124px; }
  .wing-left h3 { font-size: 9px; font-weight: 700; letter-spacing: .1px; padding-bottom: 6px; border-bottom: 1px solid var(--rule); margin-bottom: 6px; }
  .wing-left p { font-size: 9.5px; line-height: 15.4px; text-align: justify; hyphens: auto; }

  .front { position: absolute; top: 0; width: 394px; height: 100%; text-align: center; }
  .label--full .front { left: 142px; }
  .label--front .front { left: 0; }

  .brand-name { font-family: var(--sans); font-weight: 700; color: var(--brand); line-height: 1; }
  .brand-name .line1 { display: block; font-size: 25px; letter-spacing: 1px; text-transform: uppercase; }
  .brand-name .line2 { display: block; font-size: 19px; margin-top: 2px; }
  .seal .brand-name .line1 { font-size: 20px; }
  .seal .brand-name .line2 { font-size: 15px; }

  .front .mark { position: absolute; left: 50%; top: 14px; width: 24px; height: 24px; margin-left: -12px; border-radius: 50%; border: 2px solid var(--brand); }
  .front .brand-name { position: absolute; left: 0; right: 0; top: 110px; }
  .product-name { position: absolute; left: 0; right: 0; top: 198px; font-family: var(--serif); font-size: 29px; letter-spacing: 1.5px; text-transform: uppercase; color: var(--ink); }

  .variety-band { position: absolute; left: -1px; right: -1px; top: 246px; height: 19px; color: #fff;
    font-size: 11.5px; font-weight: 700; letter-spacing: .8px; text-align: center; line-height: 19px; }
  .variety-band--summer { background: var(--yellow); }
  .variety-band--rape { background: var(--green); }

  .wing-right { position: absolute; left: 553px; top: 72px; width: 112px; font-size: 10px; line-height: 14px; }
  .wing-right .storage { padding-bottom: 8px; border-bottom: 1px solid var(--rule); margin-bottom: 10px; }
  .wing-right .address { padding-bottom: 10px; border-bottom: 1px solid var(--rule); }
  .wing-right .weight { font-size: 22px; margin-top: 22px; }
</style>
</head>
<body>
<div class="canvas">

  <!-- Sommertrachthonig: seal and full wrap label -->
  <div class="seal">
    <div class="brand-name"><span class="line1">Fam. Halvers</span><span class="line2">Imkerei</span></div>
    <div class="divider"></div>
    <div class="mhd-label">Mindestens haltbar bis:</div>
    <div class="mhd-date">10.06.2024</div>
  </div>
  <div class="tab tab-yellow"></div>
  <div class="tab-white" style="left:322px; top:440px; width:118px; height:115px;"></div>

  <section class="label label--full">
    <div class="comb" role="img" aria-label="Wabenmuster" style="left:0; top:0; width:142px; height:60px;"></div>
    <div class="comb" role="img" aria-label="Wabenmuster" style="left:142px; top:0; width:120px; height:110px;"></div>
    <div class="comb" role="img" aria-label="Wabenmuster" style="left:420px; top:150px; width:120px; height:90px; transform:scaleX(-1);"></div>
    <div class="comb" role="img" aria-label="Wabenmuster" style="left:590px; top:0; width:84px; height:60px; transform:scaleX(-1);"></div>

    <div class="wing-left">
      <h3>DEUTSCHER QUALITÄTSHONIG</h3>
      <p>Lorem ipsum dolor sit amet, consectetuer adipiscing elit, sed diam nonummy nibh eu ismod tincidunt es ut laoreet dolore magna aliquam erat volutpat. Ut wisi enim ad minim veniam, quis nostrud exerci tation ullamcorper suscipit lobortis nisl ut aliquip ex ea commodo con sequat uis autem vel eumes.</p>
    </div>

    <div class="front">
      <span class="mark"></span>
      <div class="brand-name"><span class="line1">Fam. Halvers</span><span class="line2">Imkerei</span></div>
      <div class="product-name">Dünenglanz</div>
    </div>

    <div class="wing-right">
      <p class="storage">Trocken, Dunkel und vor Wärme geschützt lagern</p>
      <p class="address">Imkerei Halvers<br>Strassenname 00<br>D-22665 Ortschaft<br>imkerei-halvers.de</p>
      <p class="weight">250g</p>
    </div>

    <div class="variety-band variety-band--summer">SOMMERTRACHTHONIG</div>
  </section>

  <!-- Rapshonig: front label -->
  <div class="tab tab-green"></div>
  <div class="tab-white" style="left:915px; top:433px; width:118px; height:122px;"></div>

  <section class="label label--front">
    <div class="comb" role="img" aria-label="Wabenmuster" style="left:0; top:0; width:120px; height:110px;"></div>
    <div class="comb" role="img" aria-label="Wabenmuster" style="left:260px; top:150px; width:120px; height:90px; transform:scaleX(-1);"></div>
    <div class="front">
      <span class="mark"></span>
      <div class="brand-name"><span class="line1">Fam. Halvers</span><span class="line2">Imkerei</span></div>
      <div class="product-name">Dünenglanz</div>
    </div>
    <div class="variety-band variety-band--rape">RAPSHONIG</div>
  </section>

</div>
</body>
</html>
```